Company Flyer for Electric boating company

I am looking for a company flyer which we can hand over to boat owners in the Netherlands (Amsterdam area). Our core business is to rebuild every boat (from 4 to 10 meters) into an electrically propelled boat. We are taking out diesels and replace them with a high quality electrical motor, inboard varying from 30 till 80 pk (hp). And outboard from 1pk (hp) till 200pk. We are the best, not the cheapest, not the most expensive. We only work with the best materials. The flyer has to be sort of in line with our website and branding.

Major advantages of electric boating are:
- completely silent
- no fumes, smells or smoke
- cheap to operate
- environmentally friendly
- obliged in more and more areas
- no maintenance
- more enjoyable

The flyer should be A5 format. Since all the text has to be in Dutch I expect only the graphical design and layout for advantages, process, pricing and contact details etc.

Target Market(s)

Boat owners in the Netherlands

Font styles to use
Sans Serif

Colors
9bcb3c
add136
cadf82
0555a3
3176b5
85acd3
e0ebf3

Requirements
Must have
• Clean design, in line with website: www.stroomkade.nl
Nice to have
• icons for advantages, boating etc

2 sides
Should not have
• Steering wheel...

```html
<!DOCTYPE html>
<html lang="nl">
<head>
<meta charset="utf-8">
<title>Stroomkade – Elektrisch Varen flyer</title>
<link href="https://fonts.googleapis.com/css2?family=Montserrat:wght@300;400;500;600;700;800&family=Oswald:wght@400;500&display=swap" rel="stylesheet">
<style>
:root{
  --green:#84bd00;
  --green-bright:#8fc31f;
  --navy:#3a3f56;
  --navy-deep:#2b3044;
  --ink:#2f3242;
  --grey-text:#55596a;
  --paper:#ffffff;
  --paper-soft:#f2f3f5;
  --stage:#5b5b5b;
}
*{box-sizing:border-box;margin:0;padding:0}
html,body{width:1200px;height:900px;overflow:hidden}
body{background:radial-gradient(ellipse at 50% 0%,#3a3a3a 0%,#5b5b5b 60%,#6a6a6a 100%);font-family:'Montserrat',sans-serif;position:relative}
.sheet{position:absolute;background:var(--paper);overflow:hidden;box-shadow:0 6px 18px rgba(0,0,0,.35)}
.abs{position:absolute}

/* ---------- front ---------- */
.front{left:78px;top:99px;width:495px;height:702px}
.header-shape{left:0;top:0;width:495px;height:102px}
.brand{left:30px;top:30px;display:flex;align-items:center;gap:12px}
.brand-dot{width:44px;height:44px;border-radius:50%;background:var(--navy)}
.brand-name{font-weight:700;font-size:24px;color:var(--green);line-height:1;letter-spacing:.5px}
.brand-tag{font-weight:400;font-size:9px;letter-spacing:2.6px;color:var(--ink);margin-top:5px}
.header-contact{left:344px;top:37px;width:146px;color:#fff;font-weight:600;font-size:12.4px;line-height:24px;white-space:nowrap}
.header-contact .row{display:flex;align-items:center;gap:5px}
.hero{left:0;top:102px;width:495px;height:255px;background:radial-gradient(ellipse at 50% 30%,#6e7a86 0%,#2d343e 45%,#0d1117 100%)}
.headline{left:0;top:186px;width:495px;text-align:center;color:#fff;font-size:33px;line-height:39px;text-transform:uppercase}
.headline b{font-weight:800}
.headline span{font-weight:300}
.headline .hl{color:var(--green);font-weight:800}
.claim{left:33px;top:313px;width:429px;height:21px;background:var(--green);color:#fff;font-weight:700;font-size:11.3px;text-align:center;line-height:21px;white-space:nowrap}
.adv-band{left:0;top:357px;width:495px;height:36px;background:var(--navy);color:#fff;font-size:20px;font-weight:300;line-height:36px;padding-left:34px;white-space:nowrap}
.adv-band b{color:var(--green);font-weight:800}
.adv-area{left:0;top:393px;width:495px;height:240px;background:linear-gradient(135deg,#f7f8f9,#e9ebee)}
.adv{display:flex;align-items:center;gap:6px;font-size:12px;font-weight:500;color:var(--ink);line-height:14.5px}
.adv svg{width:30px;height:30px;flex:none}
.adv .rule{width:1px;height:34px;background:var(--green);margin-right:6px}
.tech-drawing{left:336px;top:402px;width:120px;height:177px;background:linear-gradient(160deg,#d5d8dd,#9da2aa);border-radius:6px}
.photos{left:0;top:633px;width:495px;height:69px;background:var(--navy)}
.photo{top:588px;width:103px;height:78px;border:2px solid #fff}
.p1{left:29px;background:linear-gradient(#9fb4c7,#3e5667)}
.p2{left:140px;background:linear-gradient(#b6c4cf,#47596a)}
.p3{left:251px;background:linear-gradient(#aab8c2,#2f3b44)}
.p4{left:363px;background:linear-gradient(#c8d6e2,#4d6880)}
.front-footer{left:26px;top:673px;color:#fff;font-size:11px;display:flex;align-items:center;gap:8px;white-space:nowrap}
.front-footer svg{width:10px;height:10px}

/* ---------- back ---------- */
.back{left:626px;top:97px;width:497px;height:705px}
.back-title{left:0;top:0;width:497px;height:50px;background:var(--green);color:#fff;font-family:'Oswald',sans-serif;font-weight:400;font-size:19.5px;text-align:center;line-height:50px;white-space:nowrap}
.process-bg{left:0;top:50px;width:497px;height:277px;background:linear-gradient(180deg,#3d4660 0%,#2a3148 60%,#1f2638 100%)}
.process-lead{left:0;top:62px;width:497px;text-align:center;color:#e6e8ee;font-size:9.6px;font-weight:400;white-space:nowrap}
.process svg{position:absolute;left:0;top:0}
.step-label{color:#fff;font-weight:600;font-size:10.5px;text-align:center;width:140px;line-height:13px;letter-spacing:.3px}
.price-banner{left:31px;top:311px;width:435px;height:33px;background:var(--green);color:#fff;font-weight:700;font-size:23px;text-align:center;line-height:33px;letter-spacing:.5px;white-space:nowrap}
.price-lead{left:30px;top:353px;width:437px;text-align:center;font-size:12px;color:var(--ink);line-height:17px}
.card{top:395px;width:103px;height:261px;border:1.5px solid var(--navy);border-radius:4px;background:#fff;overflow:hidden}
.card .icon{height:54px;display:flex;align-items:center;justify-content:center}
.card .band{height:60px;background:var(--navy);color:#fff;text-align:center;padding-top:5px}
.card .name{font-weight:700;font-size:12.5px;line-height:14px}
.card .sub{font-size:8px;font-weight:300;line-height:9px;margin-top:1px}
.card .price{position:absolute;left:13px;top:91px;width:75px;height:24px;background:var(--green);color:#fff;text-align:center}
.card .price small{display:block;font-size:6px;line-height:7px;padding-top:1px}
.card .price strong{display:block;font-size:12px;font-weight:700;line-height:14px}
.card .price.ask{font-size:8px;font-weight:700;line-height:24px}
.card ul{list-style:none;text-align:center;font-size:8.4px;color:var(--grey-text);margin-top:17px;line-height:10px}
.card li{margin-bottom:5.5px;white-space:nowrap}
.card li.wrap{white-space:normal}
.back-footer{left:0;top:671px;width:497px;height:34px;background:var(--navy);color:#fff;font-size:12px;display:flex;align-items:center;justify-content:center;gap:16px;white-space:nowrap}
.back-footer .item{display:flex;align-items:center;gap:5px}
.back-footer svg{width:10px;height:10px}
</style>
</head>
<body>

<section class="sheet front">
  <svg class="abs header-shape" viewBox="0 0 495 102">
    <rect width="495" height="102" fill="#fff"/>
    <polygon points="322,102 370,0 380,0 332,102" fill="var(--navy)"/>
    <polygon points="331,102 379,0 495,0 495,102" fill="var(--green)"/>
  </svg>
  <div class="abs brand">
    <div class="brand-dot"></div>
    <div>
      <div class="brand-name">STROOMKADE</div>
      <div class="brand-tag">ELEKTRISCH VAREN</div>
    </div>
  </div>
  <div class="abs header-contact">
    <div class="row"><svg width="10" height="10" viewBox="0 0 10 10" fill="none" stroke="#fff" stroke-width="1"><circle cx="5" cy="5" r="4.2"/><ellipse cx="5" cy="5" rx="1.8" ry="4.2"/><line x1=".8" y1="5" x2="9.2" y2="5"/></svg>www.stroomkade.nl</div>
    <div class="row"><svg width="10" height="10" viewBox="0 0 10 10" fill="none" stroke="#fff" stroke-width="1"><circle cx="5" cy="5" r="4.2"/><path d="M3.3 2.8c0 2.2 1.7 4 3.9 4l.3-1-1-.5-.5.5c-.8-.3-1.4-1-1.7-1.7l.5-.5-.5-1z"/></svg>+31 6 12 345 678</div>
  </div>

  <div class="abs hero" role="img" aria-label="Photo of the stern of a speedboat with two electric outboard motors churning white water"></div>
  <h1 class="abs headline">
    <b>Rebuild</b> <span>your</span> <b class="hl">boat</b><br>
    <span>into an</span> <b class="hl">electrically</b><br>
    <b>propelled boat</b>
  </h1>
  <div class="abs claim">WE ARE THE BEST, NOT THE CHEAPEST, NOT THE MOST EXPENSIVE.</div>

  <div class="abs adv-band">ADVANTAGES OF <b>ELECTRIC BOATING ARE:</b></div>
  <div class="abs adv-area"></div>

  <div class="abs adv" style="left:30px;top:415px">
    <svg viewBox="0 0 30 30" fill="none" stroke="var(--green)" stroke-width="1.4"><path d="M4 12h5l7-6v18l-7-6H4z"/><path d="M19 11c2 2 2 6 0 8M22 8c4 4 4 10 0 14"/></svg>
    <span class="rule"></span><span>Completely<br>Silent</span>
  </div>
  <div class="abs adv" style="left:30px;top:476px">
    <svg viewBox="0 0 30 30" fill="none" stroke="var(--green)" stroke-width="1.4"><rect x="3" y="8" width="24" height="12"/><circle cx="15" cy="14" r="3.5"/><path d="M10 23h4M14 23v4M20 21v5"/></svg>
    <span class="rule"></span><span>Cheap<br>To Operate</span>
  </div>
  <div class="abs adv" style="left:30px;top:539px">
    <svg viewBox="0 0 30 30" fill="none" stroke="var(--green)" stroke-width="1.4"><path d="M3 17h24l-4 5H7z"/><path d="M9 17v-4h9l3 4M12 13v-3h5"/></svg>
    <span class="rule"></span><span>More<br>Enjoyable</span>
  </div>
  <div class="abs adv" style="left:168px;top:415px">
    <svg viewBox="0 0 30 30" fill="none" stroke="var(--green)" stroke-width="1.4"><circle cx="15" cy="15" r="12"/><circle cx="15" cy="15" r="7"/><path d="M15 3v24M3 15h24M15 15l7-7"/></svg>
    <span class="rule"></span><span>Obliged In More<br>And More Areas</span>
  </div>
  <div class="abs adv" style="left:168px;top:454px">
    <svg viewBox="0 0 30 30" fill="none" stroke="var(--green)" stroke-width="1.4"><path d="M6 24L20 10M20 10c-1-3 1-6 4-6l-2 3 2 2 3-2c0 3-3 5-6 4"/><path d="M24 24L10 10l-2-4-3-1 1 3 4 2"/></svg>
    <span class="rule"></span><span>No Maintenance</span>
  </div>
  <div class="abs adv" style="left:168px;top:493px">
    <svg viewBox="0 0 30 30" fill="none" stroke="var(--green)" stroke-width="1.4"><rect x="5" y="16" width="16" height="9" rx="3"/><path d="M10 14c-2-3 2-5 0-8M15 14c-2-3 2-5 0-8M4 26L26 4"/></svg>
    <span class="rule"></span><span>No Fumes, Smells<br>Or Smoke</span>
  </div>
  <div class="abs adv" style="left:168px;top:539px">
    <svg viewBox="0 0 30 30" fill="none" stroke="var(--green)" stroke-width="1.4"><path d="M15 20V8M15 12c-3-1-4-4-4-6 3 0 4 3 4 6zM15 14c3-1 4-4 4-6-3 0-4 3-4 6z"/><path d="M3 14l3 10 5 3M27 14l-3 10-5 3"/></svg>
    <span class="rule"></span><span>Environmentally<br>Friendly</span>
  </div>

  <div class="abs tech-drawing" role="img" aria-label="Technical wireframe drawing of an inboard electric motor"></div>

  <div class="abs photos"></div>
  <div class="abs photo p1" role="img" aria-label="Photo of a dark sloop moored in a harbour"></div>
  <div class="abs photo p2" role="img" aria-label="Photo of a small boat with passengers in a marina"></div>
  <div class="abs photo p3" role="img" aria-label="Photo of a classic black boat at a quay"></div>
  <div class="abs photo p4" role="img" aria-label="Photo of a sloop on a city canal"></div>

  <div class="abs front-footer">
    <svg viewBox="0 0 10 10" fill="none" stroke="var(--green)" stroke-width="1.2"><path d="M5 9.5S1.8 6 1.8 4a3.2 3.2 0 016.4 0C8.2 6 5 9.5 5 9.5z"/><circle cx="5" cy="4" r="1.1"/></svg>
    <span>Kadeweg 12, 1000AA, Amsterdam, Nederland</span>
    <span style="margin:0 8px">|</span>
    <svg viewBox="0 0 10 10" fill="none" stroke="var(--green)" stroke-width="1"><rect x=".8" y="2" width="8.4" height="6"/><path d="M.8 2L5 5.5 9.2 2"/></svg>
    <span>info@stroomkade.nl</span>
  </div>
</section>

<section class="sheet back">
  <h2 class="abs back-title">HOE WERKT HET ELEKTRISCH OMBOUWEN VAN EEN BOOT?</h2>
  <div class="abs process-bg" role="img" aria-label="Dusk photo of an Amsterdam waterfront with a dark blue overlay"></div>
  <p class="abs process-lead">HET OMBOUWEN VAN JOUW BOOT IS EEN PROJECT WAAR WIJ JE GRAAG BIJ BETREKKEN</p>

  <div class="process">
    <svg width="497" height="327" viewBox="0 0 497 327" fill="none">
      <defs>
        <marker id="arrowhead" markerWidth="5" markerHeight="5" refX="4" refY="2.5" orient="auto"><path d="M0 0L4 2.5 0 5" stroke="#fff" stroke-width=".8" fill="none"/></marker>
      </defs>
      <g stroke="#fff" stroke-width=".8" stroke-dasharray="2 1.5" marker-end="url(#arrowhead)">
        <line x1="91" y1="163" x2="91" y2="190"/>
        <line x1="115" y1="227" x2="222" y2="227"/>
        <line x1="248" y1="193" x2="248" y2="163"/>
        <line x1="272" y1="116" x2="380" y2="116"/>
        <line x1="406" y1="163" x2="406" y2="190"/>
      </g>
      <g stroke="#fff" stroke-width=".9" stroke-dasharray="2 2" opacity=".8">
        <circle cx="91" cy="116" r="23"/><circle cx="248" cy="116" r="23"/><circle cx="406" cy="116" r="23"/>
        <circle cx="91" cy="227" r="23"/><circle cx="248" cy="227" r="23"/><circle cx="406" cy="227" r="23"/>
      </g>
      <g stroke="var(--green)" stroke-width="1.3">
        <path d="M79 108h16v10h-10l-4 4v-4h-2zM97 112h4v9h-2v3l-3-3h-6"/>
        <path d="M255 105c-6 1-11 6-13 13l3 3c7-2 12-7 13-13zM243 118l-4 1 2-5 4-1M245 121l-1 4 5-2 1-4M240 124l-3 3"/>
        <rect x="398" y="106" width="16" height="20" rx="1"/><path d="M402 104h8v4h-8zM401 117h3l2-4 2 7 2-3h3"/>
        <circle cx="85" cy="232" r="5"/><circle cx="97" cy="232" r="5"/><path d="M82 227l2-8h3l1 8M100 227l-2-8h-3l-1 8M89 229h4"/>
        <path d="M239 236l14-14M253 222c-1-3 1-5 4-5l-2 2 1 2 2-1c0 3-2 4-5 3M257 236l-14-14-2-3"/>
        <path d="M395 221h7M412 221h3v12h-7M395 221v12h5M408 218l-5 10h5l-3 8"/>
      </g>
    </svg>
    <div class="abs step-label" style="left:21px;top:147px">KENNISMAKING</div>
    <div class="abs step-label" style="left:178px;top:147px">NIEUW ERIN</div>
    <div class="abs step-label" style="left:336px;top:147px">TEST &amp; OVERDRACHT</div>
    <div class="abs step-label" style="left:21px;top:257px">PLANNING EN START<br>VAN HET PROJECT</div>
    <div class="abs step-label" style="left:178px;top:264px">OUD ERUIT</div>
    <div class="abs step-label" style="left:336px;top:257px">VAREN<br>EN SERVICE</div>
  </div>

  <div class="abs price-banner">PRIJZEN VOOR HET OMBOUWEN</div>
  <p class="abs price-lead">RICHTPRIJZEN VAN ONZE STANDAARD PAKKETTEN WAARMEE U MINIMAAL 8 UUR KUNT VAREN.</p>

  <div class="abs card" style="left:34px">
    <div class="icon"><svg width="76" height="26" viewBox="0 0 76 26" fill="none" stroke="var(--ink)" stroke-width="1.3"><path d="M2 6h72l-3 11c-20 4-45 5-67 5L2 6z"/><path d="M4 22v2"/><rect x="8" y="9" width="10" height="7" fill="#fff"/><rect x="18" y="11" width="2" height="3"/></svg></div>
    <div class="band"><div class="name">KLEIN</div><div class="sub">tot 5 mtr</div></div>
    <div class="price"><small>vanaf</small><strong>€2200</strong></div>
    <ul><li>Outboard</li><li>1,1kW motor (4pk)</li><li>915 Wh Li-Ion</li><li>GPS tracker</li><li>Draagbare accu</li><li>zelf te monteren</li><li class="wrap">perfecte<br>vervanging voor<br>buitenboordmotor</li></ul>
  </div>
  <div class="abs card" style="left:143px">
    <div class="icon"><svg width="76" height="26" viewBox="0 0 76 26" fill="none" stroke="var(--ink)" stroke-width="1.3"><path d="M2 6h72l-3 11c-20 4-45 5-67 5L2 6z"/><path d="M4 22v2"/><rect x="8" y="9" width="12" height="7" fill="#fff"/><rect x="20" y="11" width="2" height="3"/></svg></div>
    <div class="band"><div class="name">MIDDEL</div><div class="sub">5 mtr tot 8,5 mtr</div></div>
    <div class="price"><small>vanaf</small><strong>€12500</strong></div>
    <ul><li>Inboard</li><li>8,5kW | 81Nm | 35pk*1</li><li>12kW accupakket</li><li>inclusief inbouw</li><li>Inclusief lader</li><li>Zuinig &amp; Krachtig</li><li>IP 67 waterproof</li></ul>
  </div>
  <div class="abs card" style="left:251px">
    <div class="icon"><svg width="76" height="26" viewBox="0 0 76 26" fill="none" stroke="var(--ink)" stroke-width="1.3"><path d="M2 6h72l-3 11c-20 4-45 5-67 5L2 6z"/><path d="M4 22v2"/><rect x="8" y="9" width="14" height="7" fill="#fff"/><rect x="22" y="11" width="2" height="3"/></svg></div>
    <div class="band"><div class="name">GROOT</div><div class="sub">7 mtr tot 10 mtr</div></div>
    <div class="price"><small>vanaf</small><strong>€17500</strong></div>
    <ul><li>Inboard</li><li style="font-size:7.9px">17,5kW | 209Nm | 55pk*1</li><li>20kW accupakket</li><li>inclusief inbouw</li><li>Inclusief lader</li><li>Zuinig &amp; Krachtig</li><li>IP 67 waterproof</li></ul>
  </div>
  <div class="abs card" style="left:360px">
    <div class="icon"><svg width="76" height="26" viewBox="0 0 76 26" fill="none" stroke="var(--ink)" stroke-width="1.3"><path d="M2 6h72l-3 11c-20 4-45 5-67 5L2 6z"/><path d="M4 22v2"/><rect x="8" y="9" width="13" height="7" fill="#fff"/><rect x="22" y="9" width="13" height="7" fill="#fff"/><rect x="36" y="9" width="13" height="7" fill="#fff"/><rect x="49" y="11" width="2" height="3"/></svg></div>
    <div class="band"><div class="name">ANDERS</div><div class="sub">vanaf 10 meter of<br>snelvarend</div></div>
    <div class="price ask">OP AANVRAAG</div>
    <ul><li>Inboard en Outboard</li><li>Maatwerk</li><li>Elke Capaciteit</li><li>Inbouw op maat</li><li class="wrap">Laag,- en<br>hoogspanning</li><li>Ook voor advies</li><li>Partnernetwerk</li></ul>
  </div>

  <footer class="abs back-footer">
    <span class="item"><svg viewBox="0 0 10 10" fill="none" stroke="var(--green)" stroke-width="1"><circle cx="5" cy="5" r="4.2"/><ellipse cx="5" cy="5" rx="1.8" ry="4.2"/><line x1=".8" y1="5" x2="9.2" y2="5"/></svg>www.stroomkade.nl</span>
    <span>|</span>
    <span class="item"><svg viewBox="0 0 10 10" fill="none" stroke="var(--green)" stroke-width="1"><circle cx="5" cy="5" r="4.2"/><path d="M3.3 2.8c0 2.2 1.7 4 3.9 4l.3-1-1-.5-.5.5c-.8-.3-1.4-1-1.7-1.7l.5-.5-.5-1z"/></svg>+31 6 12 345 678</span>
    <span>|</span>
    <span class="item"><svg viewBox="0 0 10 10" fill="none" stroke="var(--green)" stroke-width="1"><rect x=".8" y="2" width="8.4" height="6"/><path d="M.8 2L5 5.5 9.2 2"/></svg>info@stroomkade.nl</span>
  </footer>
</section>

</body>
</html>
```